Sales Brochure- Generic Line Card 215mm x 140mm

Design a double-sided brochure similar to the attached sample. Cover Page contains a logo and theme that never changes. However, the background picture and the description text on the lower corner will be changed to advertise multiple services. Reverse-side contains Detailed Descriptive text related to the picture on Cover Page as well as Logo and Contact information for the business. Use the Ridgeline Controls website www.ridgelinecontrols.ca for theme, color and contact information. Also, use attached business card design for theme to match. Use the supplied logo. SIZE 215mm x 140mm

Font styles to use
Sans Serif

Colors

Designer to choose colors to be used in the design.

Requirements
Must have
• Look Similar to Sample Brochure but include Ridgeline Controls theme and colors

```html
<!DOCTYPE html>
<html lang="en">
<head>
<meta charset="utf-8">
<title>Ridgeline Controls – Line Card</title>
<link href="https://fonts.googleapis.com/css2?family=Jost:wght@300;400;500;700&display=swap" rel="stylesheet">
<style>
:root{
  --page:#eeeeee;
  --teal:#1f8a86;
  --teal-deep:#0f5553;
  --teal-dark:#0b3b3a;
  --ink:#161616;
  --charcoal:#262626;
  --strip:#1b1b1b;
  --white:#ffffff;
  --orange:#f15a1f;
  --grey-text:#d8d8d8;
}
*{box-sizing:border-box;margin:0;padding:0}
html,body{width:898px;height:1200px;overflow:hidden;background:var(--page);font-family:"Jost",Arial,sans-serif;color:var(--white)}
.card{position:absolute;width:595px;height:387px;overflow:hidden}
.front{left:154px;top:149px;background:var(--strip)}
.back{left:149px;top:660px;background:var(--charcoal)}

.front-photo{position:absolute;left:55px;top:0;width:540px;height:387px;
  background:radial-gradient(circle at 78% 22%,#2aa39d 0%,#1a7d79 38%,#10524f 70%,#0a2f2e 100%)}
.front-shade{position:absolute;left:0;bottom:0;width:595px;height:120px;background:linear-gradient(to bottom,rgba(0,0,0,0),rgba(0,0,0,.35))}

.brand-box{position:absolute;background:var(--white);display:flex;align-items:center;justify-content:center;gap:8px}
.front .brand-box{left:55px;top:0;width:221px;height:77px}
.brand-mark{width:14px;height:14px;background:var(--teal)}
.brand-name{font-weight:700;font-size:17px;letter-spacing:.5px;color:var(--ink);text-transform:uppercase;white-space:nowrap}

.rule{position:absolute;left:105px;top:147px;width:2px;height:240px;background:var(--white)}
.headline{position:absolute;left:123px;top:140px;line-height:1.05;text-transform:uppercase}
.headline .light{display:block;font-weight:300;font-size:28px}
.headline .bold{display:block;font-weight:700;font-size:34px;letter-spacing:.5px}

.sectors{position:absolute;left:344px;top:312px;display:flex;gap:0}
.sector{width:38px;text-align:center;font-size:9px;font-weight:400}
.sector svg{display:block;margin:0 auto 9px;width:22px;height:24px;stroke:var(--white);fill:none;stroke-width:1.3}
.sector.wide{width:52px}

.back-photo{position:absolute;inset:0;background:radial-gradient(circle at 85% 25%,#4a4a4a 0%,#2c2c2c 45%,#1c1c1c 100%)}
.intro{position:absolute;left:37px;top:32px;width:530px}
.intro h2{font-size:12px;font-weight:700;margin-bottom:2px}
.intro p{font-size:9px;font-weight:400;line-height:1.3;color:var(--grey-text)}

.services{position:absolute;left:37px;top:107px;display:flex;gap:11px}
.service{width:94px}
.service-photo{height:62px;background:linear-gradient(135deg,#8a8a8a,#3a3a3a 55%,#1a1a1a)}
.service-label{height:21px;background:var(--orange);font-size:10px;font-weight:400;display:flex;align-items:center;justify-content:center;text-transform:uppercase}
.service:first-child .service-label{justify-content:flex-start;padding-left:5px}

.capabilities{position:absolute;left:37px;top:212px;display:flex;gap:30px}
.capabilities ul{list-style:none;font-size:9.3px;line-height:12px;color:var(--grey-text)}
.capabilities li::before{content:"•";margin-right:6px}
.capabilities ul:first-child{width:190px}

.contact-band{position:absolute;left:0;bottom:0;width:595px;height:55px;background:linear-gradient(90deg,var(--teal-deep),var(--teal) 60%,var(--teal-deep))}
.back .brand-box{left:37px;top:313px;width:215px;height:74px}
.back .brand-name{font-size:16px}
.drop-line{position:absolute;left:274px;top:347px;font-size:10.5px;font-weight:700;line-height:14px;text-transform:uppercase}
.contact{position:absolute;left:337px;top:344px;font-size:10px;line-height:18px}
.contact div{display:flex;align-items:center;gap:6px}
.contact svg{width:10px;height:10px;fill:var(--white)}
.contact .gap{margin-left:10px}
</style>
</head>
<body>

<section class="card front">
  <div class="front-photo" role="img" aria-label="Teal-toned close-up of a CNC lathe turret and machined shaft"></div>
  <div class="front-shade"></div>
  <div class="brand-box"><span class="brand-mark"></span><span class="brand-name">Ridgeline Controls</span></div>
  <div class="rule"></div>
  <h1 class="headline">
    <span class="light">Pioneering</span>
    <span class="bold">Responsive</span>
    <span class="light">Machining</span>
  </h1>
  <div class="sectors">
    <div class="sector">
      <svg viewBox="0 0 22 24"><path d="M11 10v13M11 10L4 6M11 10l7-4M11 10V2"/><circle cx="11" cy="10" r="1.2"/></svg>Energy
    </div>
    <div class="sector wide">
      <svg viewBox="0 0 22 24"><rect x="5" y="2" width="12" height="20"/><path d="M5 8h12M5 16h12"/></svg>Oil &amp; Gas
    </div>
    <div class="sector">
      <svg viewBox="0 0 22 24"><path d="M3 5c6-3 12 0 16 6M7 5l12 16"/></svg>Mining
    </div>
    <div class="sector wide">
      <svg viewBox="0 0 22 24"><path d="M2 22V7l5-4 5 4v15M12 22V9l4-3 4 3v13M5 10h4M5 14h4M5 18h4M14 12h4M14 16h4"/></svg>Architecture
    </div>
    <div class="sector">
      <svg viewBox="0 0 22 24"><circle cx="6" cy="18" r="4"/><circle cx="18" cy="19" r="2.5"/><path d="M4 13V6h7l2 6h7v5M13 12H4"/></svg>Agri
    </div>
  </div>
</section>

<section class="card back">
  <div class="back-photo" role="img" aria-label="Dark grey close-up of CNC machining equipment"></div>
  <div class="intro">
    <h2>COMPUTER NUMERIC CONTROL (CNC)</h2>
    <p>CNC machining offers the most efficient method of producing steel and plastic components.<br>
    The CNC is programmed using computer code to generate a digital machining process that can be repeated and precisely controlled. Repetitive tasks such as drilling, threading, and tapping are made simple using this technology.</p>
  </div>
  <div class="services">
    <div class="service"><div class="service-photo" role="img" aria-label="Lathe turning a metal part"></div><div class="service-label">Lathe / Turning</div></div>
    <div class="service"><div class="service-photo" role="img" aria-label="Milling cutter working a steel block"></div><div class="service-label">Milling</div></div>
    <div class="service"><div class="service-photo" role="img" aria-label="Swiss-type screw machine tooling"></div><div class="service-label">Swiss</div></div>
    <div class="service"><div class="service-photo" role="img" aria-label="Five-axis machining head"></div><div class="service-label">5-Axis</div></div>
  </div>
  <div class="capabilities">
    <ul>
      <li>Lathe &amp; Turning Centers up to 36" Dia.</li>
      <li>Mill &amp; Machining Centers up to 120" L</li>
      <li>Complex Multi-Axis Machining up to 8-Axis</li>
      <li>Swiss Screw Machining</li>
      <li>Deep Hole Drilling/Trepanning</li>
      <li>CNC Honing &amp; Grinding</li>
    </ul>
    <ul>
      <li>CNC Laser &amp; Cladding</li>
      <li>CNC Press</li>
      <li>CNC Plasma &amp; Water Jet</li>
      <li>Oil Field and Custom Threading</li>
      <li>3D Surfacing and Mold Machining</li>
      <li>Large Capacity Band Saw Cutting</li>
    </ul>
  </div>
  <div class="contact-band"></div>
  <div class="brand-box"><span class="brand-mark"></span><span class="brand-name">Ridgeline Controls</span></div>
  <div class="drop-line">Drop us<br>a line</div>
  <div class="contact">
    <div>
      <svg viewBox="0 0 10 10"><path d="M2 0l2 2.5-1.2 1.2a6 6 0 0 0 3.5 3.5L7.5 6 10 8l-1.5 2C4 10 0 6 0 1.5z"/></svg>780 555 0142
      <svg class="gap" viewBox="0 0 10 10"><rect x="0" y="3" width="10" height="7" rx="1"/><rect x="2" y="0" width="6" height="3"/></svg>888 555 0176
    </div>
    <div>
      <svg viewBox="0 0 10 10"><path d="M1 0h6l2 2v8H1z"/></svg>4120 Mercer Ave NW, Brookfield, AB, T0X 2K4
    </div>
  </div>
</section>

</body>
</html>
```